Design for new site

Hi, we need a web design for a new product calmridgeway.
This product is aimed to help people with anxiety, panic attacks and other disorders on permanently basis.
Please take a look at competitors web-sites:
http://www.brightharborpath.example/
http://www.stillmeadow.example/
Key Audiences
The intended audience for this site will be people that are looking for relief from panic and anxiety.
Key Objectives
Key object is to get prospective clients to sign up for membership and purchase our audio course.
Theme of Site
The general site theme needs to be clean and simple. The audience coming to the site in under a lot of anxiety and we don’t want to add any stress.
The site needs to flow easy from top down, with few distractions in side menus and/or columns.
Color Scheme
Suggested colors need to be light shades of blue. Blue psychology is tranquil, peaceful, and calm. This color has a tremendous stress management quality to it, making us feel cool and calm.
Or it can be shades of cool green of summer forest.
Please take a look at site mock up in attachment.

```html
<!DOCTYPE html>
<html lang="en">
<head>
<meta charset="utf-8">
<title>calmridgeway</title>
<link href="https://fonts.googleapis.com/css2?family=Open+Sans:ital,wght@0,300;0,400;0,600;0,700;1,400&family=Varela+Round&family=Noto+Serif:ital@1&display=swap" rel="stylesheet">
<style>
:root{
  --sky:#33c9fb;
  --ocean:#238cc2;
  --ocean-dark:#1e7fb3;
  --ink:#555;
  --ink-dark:#333;
  --rule:#cfcfcf;
  --footer:#434343;
  --white:#fff;
}
*{box-sizing:border-box;margin:0;padding:0}
html,body{width:891px;height:1200px;overflow:hidden;background:var(--white)}
body{position:relative;font-family:"Open Sans",sans-serif;color:var(--ink)}
.abs{position:absolute}

.site-header{left:0;top:0;width:891px;height:88px;background:var(--sky)}
.brand{left:89px;top:29px;display:flex;align-items:center;gap:8px;color:var(--white);font-size:19px;font-weight:600;letter-spacing:.2px}
.brand-mark{width:14px;height:14px;background:var(--white)}
.main-nav{right:99px;top:39px;display:flex;gap:13px;font-size:11px;font-weight:600;color:var(--white)}
.main-nav span{position:relative}
.main-nav .active:after{content:"";position:absolute;left:0;right:0;top:18px;height:3px;background:var(--ocean)}
.caret{font-size:7px;opacity:.8;margin-left:2px}

.hero{left:0;top:88px;width:891px;height:267px;background:linear-gradient(90deg,#6f8a2a,#b9b33e 30%,#7e8f3a 55%,#9aa53a 80%,#6d8a30)}
.hero-arrow{width:36px;height:36px;border:2px solid rgba(255,255,255,.85);border-radius:50%;top:194px}
.hero-caption{left:558px;top:126px;width:224px;height:192px;background:rgba(0,0,0,.82);color:var(--white);padding:12px 17px}
.hero-caption h2{font-weight:400;font-size:21px;line-height:1.2;margin-bottom:14px}
.hero-caption p{font-size:10.3px;line-height:15px;width:184px}
.btn-learn{display:inline-block;margin-top:14px;background:var(--ocean);color:var(--white);font-size:10px;font-weight:700;padding:4px 9px}
.dots{display:flex;gap:5px;margin-top:7px}
.dots i{width:6px;height:6px;border-radius:50%;background:#888}
.dots i.on{background:var(--ocean)}

.welcome{left:89px;top:379px;width:445px}
.welcome h1{font-weight:300;font-size:19px;color:var(--ink-dark);margin-bottom:8px}
.welcome h1 b{font-weight:400;color:var(--ocean);margin-left:6px}
.welcome p{font-size:13px;font-weight:300;line-height:22.4px;margin-bottom:12px;color:#444}
.welcome p.tight{line-height:20px}

.signup{left:570px;top:389px;width:219px;height:184px;background:var(--sky);box-shadow:0 10px 10px -8px rgba(0,0,0,.25)}
.signup h3{background:var(--ocean);color:var(--white);font-family:"Varela Round",sans-serif;font-size:16px;text-align:center;height:38px;line-height:38px;font-weight:400}
.field{position:absolute;left:21px;width:168px;height:25px;background:#f2f2f2;font-size:10px;font-style:italic;color:#777;padding:6px 8px}
.btn-submit{left:23px;top:137px;width:78px;height:30px;background:var(--ocean);color:var(--white);font-weight:700;font-size:13.5px;text-align:center;line-height:30px;border-bottom:2px solid var(--ocean-dark)}

.section-title{font-weight:600;font-size:16.5px;color:var(--ocean)}
.blog-head{left:88px;top:626px;width:443px;height:30px;border-bottom:1px solid var(--rule)}
.mini-arrow{width:14px;height:14px;border-radius:50%;background:#999;top:639px}
.blog-thumb{left:88px;top:668px;width:176px;height:134px;background:linear-gradient(160deg,#8a6a4a,#5a7a3a 60%,#4f6e3a)}
.article{left:290px;top:666px;width:210px}
.article h4{font-weight:400;font-size:16.5px;color:var(--ocean);margin-bottom:6px}
.article p{font-size:12px;font-weight:300;color:#444;line-height:19.2px}

.news{left:574px;top:638px;width:218px;height:182px;border:1px solid #ddd;box-shadow:0 10px 10px -8px rgba(0,0,0,.2)}
.news h3{background:var(--ocean);color:var(--white);font-family:"Varela Round",sans-serif;font-weight:400;font-size:16px;height:37px;line-height:37px;padding-left:18px}
.news-item{position:absolute;left:8px;width:196px;display:flex;gap:11px}
.avatar{width:44px;height:40px;background:linear-gradient(#e8eef2,#c7d3dc);border:1px solid #ddd;flex:none}
.news-item h5{font-weight:400;font-size:9.5px;color:var(--ocean);margin-bottom:2px}
.news-item p{font-size:5.7px;line-height:8.5px;color:#777}
.news-item p b{color:var(--ocean)}
.news-divider{left:10px;top:105px;width:194px;border-top:1px solid #ddd}

.col-head{top:868px;height:34px;border-bottom:1px solid var(--rule)}
.faq-text{left:92px;width:148px;font-size:8.6px;line-height:15px}
.faq-text a{color:var(--ocean);text-decoration:underline}
.rule{border-top:1px solid var(--rule)}
.news-copy{left:318px;top:918px;width:210px;font-size:11.8px;font-weight:300;color:#444;line-height:15px}
.news-copy span{color:var(--ocean)}
.nl-field{left:319px;width:188px;height:24px;border:1px solid var(--sky);font-size:9px;font-style:italic;color:#777;padding:5px 9px}
.nl-icon{position:absolute;right:8px;top:7px}
.btn-subscribe{left:319px;top:1061px;width:72px;height:24px;background:var(--sky);color:var(--white);font-size:12px;font-weight:600;text-align:center;line-height:24px}
.testi-photo{width:44px;height:44px;border-radius:50%;border:1px solid #ccc;background:linear-gradient(#eef1f3,#b8c0c6)}
.testi-quote{left:638px;width:125px;font-family:"Noto Serif",serif;font-style:italic;font-weight:400;font-size:7.3px;line-height:10.5px;color:#777}
.quote-mark{font-family:Georgia,serif;color:var(--ocean);font-size:15px;font-weight:700;font-style:normal;left:623px}
.testi-name{font-family:"Open Sans",sans-serif;font-style:normal;font-size:7.5px;color:#555;text-align:right;margin-top:4px}
.testi-name span{color:var(--ocean)}

.site-footer{left:0;top:1123px;width:891px;height:77px;background:var(--footer);color:var(--white)}
.footer-nav{left:87px;top:21px;display:flex;gap:14px;font-size:11.3px;font-weight:600}
.copyright{left:87px;top:42px;font-size:9.6px;color:#ddd}
.social{top:22px;width:27px;height:27px;border:2px solid var(--white);border-radius:50%}
</style>
</head>
<body>

<header class="site-header abs">
  <div class="brand abs"><span class="brand-mark"></span>calmridgeway</div>
  <nav class="main-nav abs">
    <span class="active">Home</span>
    <span>Product<span class="caret">▼</span></span>
    <span>Success Stories<span class="caret">▼</span></span>
    <span>Anxiety Test</span>
    <span>Blog</span>
    <span>About</span>
    <span>FAQ</span>
    <span>Contact Us</span>
  </nav>
</header>

<section class="hero abs" role="img" aria-label="Smiling older man in a garden with green leafy shrubs"></section>
<svg class="hero-arrow abs" style="left:37px" viewBox="0 0 36 36"><path d="M22 9 L12 18 L22 27 L19 18 Z" fill="#fff"/></svg>
<svg class="hero-arrow abs" style="left:804px" viewBox="0 0 36 36"><path d="M14 9 L24 18 L14 27 L17 18 Z" fill="#fff"/></svg>
<div class="hero-caption abs">
  <h2>Lorem Ipsum Dolor</h2>
  <p>Ut enim ad minim veniam, quis nostrud exercitation ullamco laboris nisi ut aliquip ex ea commodo consequat. Duis aute.</p>
  <span class="btn-learn">Learn More</span>
  <div class="dots"><i></i><i class="on"></i><i></i><i></i></div>
</div>

<section class="welcome abs">
  <h1>Welcome to <b>CALMRIDGEWAY</b></h1>
  <p>Lorem ipsum dolor sit amet, consectetur adipisicing elit, sed do eiusmod tempor incididunt ut labore et dolore magna aliqua. Ut enim ad minim veniam, quis nostrud exercitation ullamco laboris nisi ut aliquip ex ea commodo consequat.</p>
  <p class="tight">Labore et dolore magna aliqua. Ut enim ad minim veniam, quis nostrud exercitation ullamco laboris nisi ut aliquip ex ea commodo consequat. Duis aute irure dolor in reprehenderit in.</p>
</section>

<aside class="signup abs">
  <h3>Sign Up Now!</h3>
  <div class="field" style="top:57px">Enter your name</div>
  <div class="field" style="top:92px">Enter your Email</div>
  <div class="btn-submit abs">Submit</div>
</aside>

<div class="blog-head abs"><span class="section-title">Blog</span></div>
<svg class="mini-arrow abs" style="left:477px" viewBox="0 0 14 14"><path d="M8.5 3.5 L5 7 L8.5 10.5" stroke="#fff" stroke-width="1.8" fill="none"/></svg>
<svg class="mini-arrow abs" style="left:495px" viewBox="0 0 14 14"><path d="M5.5 3.5 L9 7 L5.5 10.5" stroke="#fff" stroke-width="1.8" fill="none"/></svg>
<div class="blog-thumb abs" role="img" aria-label="Older man sitting on a garden bench with a walking cane"></div>
<article class="article abs">
  <h4>Title of article here</h4>
  <p>Consectetur adipisicing elit, sed do eiusmod tempor incididunt ut labore et dolore magna aliqua. Ut enim ad minim veniam, quis nostrud exercita tion ullamco laboris nisi ut aliquip ex ea commodo.</p>
</article>

<aside class="news abs">
  <h3>Latest News &amp; Events</h3>
  <div class="news-item" style="top:50px">
    <div class="avatar" role="img" aria-label="Two doctors in white coats"></div>
    <div><h5>Lorem ipsum doloreum</h5><p>Lorem ipsum dolor sit amet, consectetur adipisicing elit, sed do eiusmod tempor incididunt ut labore et dol... <b>[Read More]</b></p></div>
  </div>
  <div class="news-divider abs"></div>
  <div class="news-item" style="top:118px">
    <div class="avatar" role="img" aria-label="Two doctors in white coats"></div>
    <div><h5>Lorem ipsum doloreum</h5><p>Lorem ipsum dolor sit amet, consectetur adipisicing elit, sed do eiusmod tempor incididunt ut labore et dol... <b>[Read More]</b></p></div>
  </div>
</aside>

<div class="col-head abs" style="left:90px;width:148px"><span class="section-title">FAQ</span></div>
<p class="faq-text abs" style="top:915px">Lorem ipsum dolor sit amet, consectetur adipisicing elit, sed do eiusmod tempor incididunt ut labore et dolore magna aliqua. Ut enim ad minim veniam, quis.. <a>Read More</a></p>
<div class="rule abs" style="left:90px;top:1006px;width:148px"></div>
<p class="faq-text abs" style="top:1017px">Lorem ipsum dolor sit amet, consectetur adipisicing elit, sed do eiusmod tempor incididunt ut labore et dolore magna aliqua. Ut enim ad minim veniam, quis.. <a>Read More</a></p>
<div class="rule abs" style="left:90px;top:1100px;width:148px"></div>

<div class="col-head abs" style="left:319px;width:199px"><span class="section-title">Newsletter</span></div>
<p class="news-copy abs">Sign up to our newsletter to receive discounts, news, and updates from <span>calmridgeway</span></p>
<div class="nl-field abs" style="top:975px">Name
  <svg class="nl-icon" width="10" height="10" viewBox="0 0 10 10"><circle cx="5" cy="3" r="2.4" fill="#aaa"/><path d="M0.5 10 Q5 4 9.5 10Z" fill="#aaa"/></svg></div>
<div class="nl-field abs" style="top:1010px">Email
  <svg class="nl-icon" width="10" height="8" viewBox="0 0 10 8"><rect width="10" height="8" fill="#aaa"/><path d="M0 0 L5 4.5 L10 0" stroke="#fff" fill="none"/></svg></div>
<div class="btn-subscribe abs">Subscribe</div>

<div class="col-head abs" style="left:574px;width:217px"><span class="section-title">Testimonials</span></div>
<svg class="mini-arrow abs" style="left:757px;top:874px" viewBox="0 0 14 14"><path d="M8.5 3.5 L5 7 L8.5 10.5" stroke="#fff" stroke-width="1.8" fill="none"/></svg>
<svg class="mini-arrow abs" style="left:776px;top:874px" viewBox="0 0 14 14"><path d="M5.5 3.5 L9 7 L5.5 10.5" stroke="#fff" stroke-width="1.8" fill="none"/></svg>
<div class="testi-photo abs" style="left:575px;top:918px" role="img" aria-label="Portrait of a man in a suit"></div>
<span class="quote-mark abs" style="top:912px">“</span>
<div class="testi-quote abs" style="top:922px">Lorem ipsum dolor sit amet, consectetur adipisicing elit, sed do eiusmod tempor incididunt ut.
  <div class="testi-name"><span>John Doe</span>, New York</div></div>
<div class="rule abs" style="left:572px;top:982px;width:187px"></div>
<div class="testi-photo abs" style="left:575px;top:1008px" role="img" aria-label="Portrait of a woman with glasses"></div>
<span class="quote-mark abs" style="top:1001px">“</span>
<div class="testi-quote abs" style="top:1011px">Lorem ipsum dolor sit amet, consectetur adipisicing elit, sed do eiusmod tempor incididunt ut.
  <div class="testi-name"><span>Jenna Doe</span>, New York</div></div>
<div class="rule abs" style="left:572px;top:1071px;width:187px"></div>

<footer class="site-footer abs">
  <nav class="footer-nav abs">
    <span>Home</span><span>Product</span><span>Success Stories</span><span>Anxiety Test</span><span>Blog</span><span>About</span><span>FAQ</span><span>Contact Us</span>
  </nav>
  <p class="copyright abs">Copyright©2014Anxiety project. All Rights Reserved</p>
  <span class="social abs" style="left:650px" aria-label="Social link"></span>
  <span class="social abs" style="left:688px" aria-label="Social link"></span>
  <span class="social abs" style="left:726px" aria-label="Social link"></span>
  <span class="social abs" style="left:764px" aria-label="Social link"></span>
</footer>

</body>
</html>
```